Expedited Project Word Template, envelopes and powerpoint template
no business card needed already have
n/a
2486 Quill Basin Lane
Norwalk, OH 44857
info@tivelmora.com
-uploaded logo needs to have ® symbol placed after the word "growing"
-already have business cards just need word template and letterhead and envelopes
-business focused on renewable energies/fresh produce production/environment, looking for classic corporate look
--trying to limit cost of printing as a start-up, so preference is for white background and then use color to highlight key areas
--powerpoint template looking for title slide, section break slide, main content slide, table slide, and image slide. template should include page numbering and private/confidential in the footer.
Here is how my biz card looks -- please note the tag line on this copy is correct"
"where technology and nature meet"

```html
<!DOCTYPE html>
<html lang="en">
<head>
<meta charset="utf-8">
<title>Tivelmora Growing Stationery Set</title>
<link href="https://fonts.googleapis.com/css2?family=Open+Sans:wght@400;600;700&display=swap" rel="stylesheet">
<style>
  :root {
    --backdrop: #3a2a1f;
    --paper: #ffffff;
    --brand-green: #7cb342;
    --brand-olive: #5a5a2c;
    --brand-cyan: #4fd3e3;
    --ink: #555a55;
    --ink-light: #9aa09a;
    --faint: #eef1ec;
  }
  * { box-sizing: border-box; margin: 0; padding: 0; }
  html, body { width: 1200px; height: 406px; overflow: hidden; }
  body {
    background: var(--backdrop);
    font-family: "Open Sans", Arial, sans-serif;
    color: var(--ink);
    position: relative;
  }
  .sheet { position: absolute; background: var(--paper); box-shadow: 0 2px 6px rgba(0,0,0,.45); overflow: hidden; }
  .brand { text-align: center; }
  .brand-mark { width: 11px; height: 11px; border-radius: 50%; background: var(--brand-green); margin: 0 auto 3px; }
  .brand-name { font-size: 5.5px; font-weight: 700; color: var(--brand-green); letter-spacing: .4px; }
  .brand-tag { font-size: 3.5px; color: var(--ink-light); margin-top: 1px; }
  .faint-circle { position: absolute; border-radius: 50%; background: var(--faint); }

  /* letterheads */
  .letterhead { top: 43px; width: 223px; height: 317px; }
  .letterhead--one { left: 53px; }
  .letterhead--two { left: 307px; }
  .letterhead .brand { margin-top: 14px; }
  .letterhead .faint-circle { width: 120px; height: 120px; left: 52px; top: 110px; }
  .letterhead-footer {
    position: absolute; left: 0; right: 0; bottom: 0; height: 14px;
    border-top: 1.5px solid var(--brand-green);
    font-size: 3.5px; color: var(--ink); padding: 4px 14px;
  }

  /* note card */
  .note-card { left: 569px; top: 43px; width: 163px; height: 162px; }
  .note-card .brand { margin-top: 8px; }
  .note-card .faint-circle { width: 70px; height: 70px; left: 46px; top: 32px; }
  .note-card-line { position: absolute; top: 92px; width: 100%; text-align: center; font-size: 4px; font-weight: 700; color: var(--ink); letter-spacing: .4px; }
  .note-card-web { position: absolute; bottom: 8px; width: 100%; text-align: center; font-size: 3px; color: var(--ink-light); }

  /* slide */
  .slide { left: 569px; top: 216px; width: 163px; height: 144px; }
  .slide-heading { position: absolute; left: 70px; top: 14px; font-size: 6px; color: var(--ink); }
  .slide-sub { position: absolute; left: 70px; top: 22px; font-size: 4px; color: var(--ink-light); }
  .slide-table { position: absolute; left: 12px; top: 42px; }

  /* thank you cards */
  .thanks { left: 763px; width: 161px; background: var(--brand-olive); color: #fff; }
  .thanks--front { top: 43px; height: 162px; }
  .thanks--back { top: 216px; height: 144px; }
  .thanks-title { position: absolute; left: 16px; top: 52px; font-size: 16px; font-weight: 400; letter-spacing: .5px; }
  .thanks-web { position: absolute; left: 16px; bottom: 12px; font-size: 3px; color: #d6d6c4; }

  /* envelopes */
  .envelope { left: 960px; width: 168px; }
  .envelope--flap { top: 43px; height: 66px; }
  .envelope--plain { top: 113px; height: 62px; }
  .envelope--cyan { top: 188px; height: 60px; background: var(--brand-cyan); }
  .envelope--address { top: 252px; height: 58px; }
  .envelope .flap { position: absolute; left: 0; top: 0; }
  .envelope--flap .brand-mark { position: absolute; left: 78px; top: 10px; }
  .envelope--address .brand { position: absolute; left: 10px; top: 18px; text-align: left; }
  .envelope--address .brand-mark { margin: 0 0 3px 12px; }
  .envelope--address .brand-name { font-size: 4px; }
</style>
</head>
<body>

  <section class="sheet letterhead letterhead--one">
    <div class="brand">
      <div class="brand-mark"></div>
      <div class="brand-name">TIVELMORA GROWING®</div>
      <div class="brand-tag">where technology and nature meet</div>
    </div>
    <div class="faint-circle"></div>
    <div class="letterhead-footer">2486 Quill Basin Lane, Norwalk, OH 44857 &nbsp;|&nbsp; P 419 555 0142 &nbsp;|&nbsp; info@tivelmora.com</div>
  </section>

  <section class="sheet letterhead letterhead--two">
    <div class="brand">
      <div class="brand-mark"></div>
      <div class="brand-name">TIVELMORA GROWING®</div>
      <div class="brand-tag">where technology and nature meet</div>
    </div>
    <div class="faint-circle"></div>
    <div class="letterhead-footer">2486 Quill Basin Lane, Norwalk, OH 44857 &nbsp;|&nbsp; P 419 555 0142 &nbsp;|&nbsp; info@tivelmora.com</div>
  </section>

  <section class="sheet note-card">
    <div class="brand"><div class="brand-mark"></div></div>
    <div class="faint-circle"></div>
    <p class="note-card-line">MAKE YOUR NEXT MOVE</p>
    <p class="note-card-web">www.tivelmora.com</p>
  </section>

  <section class="sheet slide">
    <p class="slide-heading">Heading Here</p>
    <p class="slide-sub">Sub Heading</p>
    <svg class="slide-table" width="140" height="40" viewBox="0 0 140 40">
      <g fill="#9aa09a">
        <rect x="0" y="0" width="60" height="2.5"/><rect x="72" y="0" width="60" height="2.5"/>
      </g>
      <g fill="#d4d8d2">
        <rect x="0" y="6" width="60" height="1.5"/><rect x="72" y="6" width="60" height="1.5"/>
        <rect x="0" y="10" width="60" height="1.5"/><rect x="72" y="10" width="60" height="1.5"/>
        <rect x="0" y="14" width="60" height="1.5"/><rect x="72" y="14" width="60" height="1.5"/>
        <rect x="0" y="18" width="60" height="1.5"/><rect x="72" y="18" width="60" height="1.5"/>
        <rect x="0" y="22" width="60" height="1.5"/><rect x="72" y="22" width="60" height="1.5"/>
      </g>
    </svg>
  </section>

  <section class="sheet thanks thanks--front">
    <p class="thanks-title">THANK YOU</p>
    <p class="thanks-web">www.tivelmora.com</p>
  </section>

  <section class="sheet thanks thanks--back">
    <p class="thanks-title">THANK YOU</p>
    <p class="thanks-web">www.tivelmora.com</p>
  </section>

  <section class="sheet envelope envelope--flap">
    <svg class="flap" width="168" height="66" viewBox="0 0 168 66">
      <polyline points="0,0 84,38 168,0" fill="none" stroke="#d8dcd6" stroke-width="0.8"/>
    </svg>
    <div class="brand-mark"></div>
  </section>

  <section class="sheet envelope envelope--plain">
    <svg class="flap" width="168" height="62" viewBox="0 0 168 62">
      <polyline points="0,0 84,30 168,0" fill="none" stroke="#d8dcd6" stroke-width="0.8"/>
    </svg>
  </section>

  <section class="sheet envelope envelope--cyan"></section>

  <section class="sheet envelope envelope--address">
    <div class="brand">
      <div class="brand-mark"></div>
      <div class="brand-name">TIVELMORA GROWING®</div>
    </div>
  </section>

</body>
</html>
```